Vent doux

Hello,
I’m a designer sunglasses reatail Store owner in Montreal, Quebec.

Looking for something modern, fresh with a trendy appeal.

Will send my logo.
Thank you.

Store

```html
<!DOCTYPE html>
<html lang="fr">
<head>
<meta charset="utf-8">
<title>Vent doux – carte professionnelle</title>
<link rel="stylesheet" href="https://fonts.googleapis.com/css2?family=Questrial&display=swap">
<style>
  :root {
    --backdrop: #1b1b1d;
    --card: #f4f4f4;
    --crimson: #c8174a;
    --crimson-light: #d8346a;
    --charcoal: #232325;
    --ink: #2b2b2d;
    --white: #ffffff;
  }
  html, body {
    margin: 0;
    width: 1200px;
    height: 900px;
    overflow: hidden;
    background: var(--backdrop);
    font-family: "Questrial", "Century Gothic", sans-serif;
  }
  .business-card {
    position: absolute;
    left: 100px;
    top: 165px;
    width: 1000px;
    height: 570px;
    border-radius: 38px;
    background: var(--card);
    overflow: hidden;
    box-shadow: 0 20px 50px rgba(0,0,0,.55);
  }
  .brand {
    position: absolute;
    left: 270px;
    top: 48px;
    display: flex;
    align-items: center;
    gap: 22px;
  }
  .brand-dot {
    width: 70px;
    height: 70px;
    border-radius: 50%;
    background: var(--crimson);
  }
  .brand-name {
    font-size: 72px;
    letter-spacing: 4px;
    color: var(--ink);
    text-transform: uppercase;
    line-height: 1;
  }
  .brand-rule {
    position: absolute;
    left: 362px;
    top: 135px;
    width: 470px;
    height: 3px;
    background: var(--crimson);
  }
  .brand-tagline {
    position: absolute;
    left: 362px;
    top: 146px;
    font-size: 30px;
    letter-spacing: 5px;
    color: var(--ink);
  }
  .name-band {
    position: absolute;
    left: 0;
    top: 215px;
    width: 700px;
    height: 88px;
    background: linear-gradient(90deg, var(--crimson), var(--crimson-light));
  }
  .holder-name {
    position: absolute;
    left: 100px;
    top: 10px;
    font-size: 34px;
    color: var(--white);
    letter-spacing: 1px;
  }
  .holder-title {
    position: absolute;
    left: 100px;
    top: 52px;
    font-size: 24px;
    color: var(--white);
  }
  .dark-band {
    position: absolute;
    left: 760px;
    top: 275px;
    width: 240px;
    height: 80px;
    background: var(--charcoal);
  }
  .seal {
    position: absolute;
    left: 628px;
    top: 178px;
    width: 150px;
    height: 150px;
    border-radius: 50%;
    background: var(--white);
    border: 11px solid var(--crimson);
    box-shadow: 0 0 0 5px var(--white);
  }
  .contact-list {
    position: absolute;
    left: 60px;
    top: 330px;
    margin: 0;
    padding: 0;
    list-style: none;
    font-size: 26px;
    color: var(--ink);
  }
  .contact-list li {
    display: flex;
    align-items: center;
    gap: 14px;
    height: 40px;
  }
  .contact-icon { width: 26px; height: 26px; }
  .shop-address {
    position: absolute;
    right: 60px;
    top: 395px;
    text-align: right;
    font-size: 28px;
    line-height: 38px;
    color: var(--ink);
  }
  .shop-address .shop-label { color: var(--crimson); }
  .bottom-stripe {
    position: absolute;
    left: 0;
    bottom: 0;
    width: 100%;
    height: 36px;
    background: var(--crimson);
    border-top: 6px solid var(--white);
    box-shadow: 0 -3px 0 var(--charcoal);
  }
</style>
</head>
<body>
  <div class="business-card">
    <div class="brand">
      <span class="brand-dot"></span>
      <span class="brand-name">Vent doux</span>
    </div>
    <div class="brand-rule"></div>
    <div class="brand-tagline">lunettes &amp; accessoires</div>

    <div class="name-band">
      <div class="holder-name">JULIEN MARCHAND</div>
      <div class="holder-title">Managing Director</div>
    </div>
    <div class="dark-band"></div>
    <div class="seal"></div>

    <ul class="contact-list">
      <li>
        <svg class="contact-icon" viewBox="0 0 26 26" aria-hidden="true">
          <circle cx="13" cy="13" r="13" fill="#c8174a"/>
          <path d="M9 7l3 3-2 2c1 2 2 3 4 4l2-2 3 3-2 2c-5 0-10-5-10-10z" fill="#fff"/>
        </svg>
        514 555-0142
      </li>
      <li>
        <svg class="contact-icon" viewBox="0 0 26 26" aria-hidden="true">
          <circle cx="13" cy="13" r="13" fill="#c8174a"/>
          <rect x="7" y="9" width="12" height="9" fill="none" stroke="#fff" stroke-width="1.6"/>
          <path d="M7 9l6 5 6-5" fill="none" stroke="#fff" stroke-width="1.6"/>
        </svg>
        514 555-0178
      </li>
      <li>
        <svg class="contact-icon" viewBox="0 0 26 26" aria-hidden="true">
          <circle cx="13" cy="13" r="13" fill="#c8174a"/>
          <circle cx="13" cy="13" r="6.5" fill="none" stroke="#fff" stroke-width="1.5"/>
          <path d="M6.5 13h13M13 6.5v13" stroke="#fff" stroke-width="1.3"/>
        </svg>
        ventdoux514@courriel.ca
      </li>
    </ul>

    <div class="shop-address">
      <div class="shop-label">Boutique Vent doux</div>
      <div>845 Rue Laurier Est</div>
      <div>Montreal, Quebec H2J3K7</div>
    </div>

    <div class="bottom-stripe"></div>
  </div>
</body>
</html>
```